I need a very simple poster with the following quote:
"Cada escolha, uma renĂșncia, isso Ă© a vida"
Which means that to every choice there is a waiver, that's life.

It will be framed and used in my living room.

The poster has to be black and white. It is not mandatory to use commas and quotes.

The design has to be modern, like the references I posted on this board: http://pinboardly.example/marvetu/ideas/

```html
<!DOCTYPE html>
<html lang="pt">
<head>
<meta charset="utf-8">
<title>Cada escolha, uma renúncia</title>
<link rel="stylesheet" href="https://fonts.googleapis.com/css2?family=Comfortaa:wght@300;400&display=swap">
<style>
  :root {
    --sky-top: #2e3131;
    --sky-glow: #6b6f6f;
    --city-mid: #3a3d3d;
    --city-deep: #1c1e1e;
    --ink: #ffffff;
  }
  html, body {
    margin: 0;
    padding: 0;
    width: 1200px;
    height: 900px;
    overflow: hidden;
    background: #000;
  }
  .poster {
    position: relative;
    width: 1200px;
    height: 900px;
    overflow: hidden;
  }
  .cityscape {
    position: absolute;
    inset: 0;
    background:
      radial-gradient(ellipse 70% 18% at 40% 26%, rgba(150,155,155,0.45), transparent 70%),
      radial-gradient(ellipse 40% 40% at 55% 70%, rgba(120,125,125,0.25), transparent 70%),
      linear-gradient(180deg,
        var(--sky-top) 0%,
        #3d4141 18%,
        var(--sky-glow) 27%,
        var(--city-mid) 38%,
        #2a2d2d 62%,
        var(--city-deep) 100%);
  }
  .quote {
    position: absolute;
    left: 0;
    top: 0;
    width: 1200px;
    height: 900px;
    margin: 0;
    color: var(--ink);
    font-family: "Comfortaa", sans-serif;
    font-weight: 300;
  }
  .quote-line {
    position: absolute;
    left: 0;
    width: 1200px;
    text-align: center;
    font-size: 126px;
    letter-spacing: 0.07em;
    line-height: 1;
    white-space: nowrap;
  }
  .line-1 { top: 270px; padding-left: 50px; box-sizing: border-box; }
  .line-2 { top: 416px; padding-left: 80px; box-sizing: border-box; }
  .line-3 { top: 562px; padding-left: 50px; box-sizing: border-box; }
  .quote-mark {
    position: absolute;
    font-family: "Comfortaa", sans-serif;
    font-weight: 400;
    font-size: 90px;
    line-height: 1;
    color: var(--ink);
  }
  .mark-open { left: 76px; top: 238px; }
  .mark-close { left: 1104px; top: 560px; }
</style>
</head>
<body>
  <main class="poster">
    <div class="cityscape" role="img" aria-label="Black and white wide-angle night view over a dense city skyline with lit skyscrapers and a long avenue below"></div>
    <blockquote class="quote">
      <span class="quote-mark mark-open">“</span>
      <span class="quote-line line-1">Cada escolha,</span>
      <span class="quote-line line-2">uma renúncia,</span>
      <span class="quote-line line-3">isso é a vida</span>
      <span class="quote-mark mark-close">”</span>
    </blockquote>
  </main>
</body>
</html>
```